single page with calendar booking ability

a single web page that has the ability to book calendar times and dates, also needs to be able to link to my other business social media seamlessly. I don't want to get multiple developers and or agency's involved, I want you the web designer to design it and make sure it's up and works as described
. The boats we work on are between 20 feet to 40 feet, bow riders , cabin cruisers, and center consoles. The brands that we work on include but are not limited to Veltora, Pirelle, Kelo marsh, Tidwick, Castavel, Brenlo, Quill, and many more. Winterization and shrink wrapping is completely different than graphic wrapping, we do not do graphic's wrapping. Also, only 5% of our business will be auto detailing, the rest will be boats on trailers. Please ensure that the calendar booking system is intergraded and not a surprise to me later

Target Market(s)

Lakes region New Hampshire

Industry/Entity Type

marine

Coding

Coded - Design and coding required

Number of Pages Required

1 page

Colors
0054AA
0677BA
7BADD7
CADEEF
E8F1F8
00AB8E
00BBA5
67D7C9
C6EFE9
E9F9F6
EE7325
F08F49
F5BC92
FAE3D3
FDF4ED

Requirements
Must have
• calendar booking capability
Nice to have
• Pictures of boats being shrink wrapped for the winter season, Nice before and after pictures of boats detailed, only 5% of our business is auto detailing
Should not have
• Large yachts, lots of sail boats as we only do a few, graphics wrapping.. we don't graphic wrap

```html
<!DOCTYPE html>
<html lang="en">
<head>
<meta charset="utf-8">
<title>Lakeline Marine</title>
<link href="https://fonts.googleapis.com/css2?family=Roboto:wght@400;500;700;900&family=Montserrat:wght@400;500;600&display=swap" rel="stylesheet">
<style>
:root{
  --blue:#0677BA;
  --blue-dark:#0054AA;
  --blue-soft:#CADEEF;
  --blue-pale:#E8F1F8;
  --orange:#EE7325;
  --orange-2:#F08F49;
  --ink:#111;
  --grey-text:#777;
  --grey-bg:#f4f4f4;
  --line:#e3e3e3;
  --white:#fff;
}
*{box-sizing:border-box;margin:0;padding:0}
html,body{width:1200px;height:3841px;overflow:hidden}
body{position:relative;font-family:'Roboto',sans-serif;color:var(--ink);background:var(--white)}
.abs{position:absolute}

/* header */
.topbar{left:392px;top:0;width:808px;height:55px;background:var(--blue)}
.topbar .follow{left:52px;top:17px;color:#fff;font-size:15px}
.topbar .soc{top:10px;width:34px;height:34px;border:2px solid #fff;border-radius:50%;display:flex;align-items:center;justify-content:center}
.topbar .call{left:386px;top:9px;display:flex;align-items:center;gap:12px;color:#fff;font-size:17px}
.call-ico{width:36px;height:36px;border-radius:50%;background:#fff;display:flex;align-items:center;justify-content:center}
.brand{left:112px;top:40px;display:flex;align-items:center;gap:10px}
.brand-dot{width:22px;height:22px;border-radius:50%;background:var(--blue)}
.brand-name{font-weight:900;font-size:36px;color:var(--orange);letter-spacing:1px}
.nav{left:474px;top:87px;display:flex;gap:27px;font-size:14.5px;font-weight:500;color:#222}
.nav .active{color:var(--orange)}

/* hero */
.hero{left:0;top:134px;width:1200px;height:678px;overflow:hidden;background:linear-gradient(180deg,#4d8fd6 0%,#8dbbe9 40%,#dbe8f1 60%,#c9cfd6 100%)}
.hero-photo{position:absolute;inset:0;background:radial-gradient(ellipse 420px 170px at 780px 470px,#f3f1ea 0%,#e6e2d8 55%,rgba(230,226,216,0) 100%)}
.hero h1{position:absolute;left:0;width:1200px;top:90px;text-align:center;font-size:51px;font-weight:700;color:#fff;letter-spacing:.5px}
.btn{display:flex;align-items:center;justify-content:center;border-radius:24px;color:#fff;font-weight:700;font-size:15px}
.hero .btn{position:absolute;left:524px;top:161px;width:151px;height:45px;background:var(--orange)}
.arrow{width:44px;height:44px;border-radius:50%;background:rgba(255,255,255,.85);display:flex;align-items:center;justify-content:center}
.dots{position:absolute;left:580px;top:484px;display:flex;gap:5px}
.dots i{width:11px;height:11px;border-radius:50%;border:2px solid #fff;display:block}
.dots i.on{background:#fff}

/* what we do */
.section-title{font-size:38px;font-weight:700;color:var(--ink)}
.wwd-title{left:0;width:1200px;top:885px;text-align:center}
.wwd-text{left:230px;width:740px;top:944px;text-align:center;font-size:13px;line-height:21.6px;color:#555}
.wwd-btn{left:524px;top:1131px;width:151px;height:45px;background:var(--blue)}

/* booking */
.booking-bg{left:0;top:1290px;width:1200px;height:650px;background:var(--grey-bg)}
.booking-title{left:112px;top:1405px}
.event{left:112px;width:462px;height:181px;background:#fff;box-shadow:0 1px 4px rgba(0,0,0,.12)}
.event .pic{position:absolute;left:4px;top:4px;width:170px;height:173px}
.event h3{position:absolute;left:198px;top:18px;width:240px;font-size:19px;font-weight:700;line-height:30px}
.event .date{position:absolute;left:198px;top:80px;font-size:13.5px;color:var(--blue);display:flex;gap:6px;align-items:center}
.event p{position:absolute;left:198px;top:104px;width:240px;font-size:13.5px;line-height:22px;color:var(--grey-text)}
.cal{left:602px;top:1496px;width:483px;height:352px;background:#fff;border:1px solid var(--line)}
.cal-head{height:58px;background:var(--blue);color:#fff;display:flex;align-items:center;justify-content:space-between;padding:0 22px;font-size:22px;font-weight:500}
.cal-grid{display:grid;grid-template-columns:repeat(7,1fr)}
.cal-grid .dn{height:15px;font-size:8px;text-align:center;color:#555;border-right:1px solid var(--line);border-bottom:1px solid var(--line)}
.cal-grid .d{height:55.6px;font-size:11px;text-align:right;padding:6px 6px 0 0;border-right:1px solid var(--line);border-bottom:1px solid var(--line);color:#222}
.cal-grid .sun{background:var(--blue-pale);color:var(--blue-dark)}
.cal-grid .sel{background:var(--blue);color:#fff;font-weight:700}
.cal-grid .book{background:var(--orange);color:#fff;font-weight:700}

/* mission */
.mission{left:0;top:1937px;width:1200px;height:620px;background:linear-gradient(180deg,#e9531f 0%,#ee6a2c 55%,#ec5e24 100%)}
.mission .kicker{position:absolute;top:90px;width:1200px;text-align:center;color:#fff;font-size:15px;font-weight:700}
.mission h2{position:absolute;top:132px;left:180px;width:840px;text-align:center;color:#fff;font-size:39.5px;line-height:43px;font-weight:700}
.mission p{position:absolute;top:366px;left:210px;width:780px;text-align:center;color:#fff;font-size:13.5px;line-height:22px}

/* blog */
.blog-title{left:0;width:1200px;top:2645px;text-align:center}
.post{top:2728px;width:312px;text-align:center;font-family:'Montserrat',sans-serif}
.post .pic{height:213px;border-radius:28px 28px 0 0}
.post h3{margin-top:16px;font-size:17px;font-weight:600;line-height:22px;padding:0 20px}
.post p{margin-top:6px;font-size:13.5px;line-height:22px;color:var(--grey-text);padding:0 22px}
.post a{display:inline-flex;gap:4px;align-items:center;margin-top:12px;font-size:14px;font-weight:600;color:var(--blue-dark);text-decoration:underline}

/* footer */
.footer{left:0;top:3275px;width:1200px;height:566px;background:#000;color:#fff}
.f-h{font-family:'Montserrat',sans-serif;font-size:16.5px;font-weight:500;color:#fff}
.field{background:#fff;font-family:'Montserrat',sans-serif;font-size:13px;color:#777;padding:10px 18px}
.submit{left:112px;top:3673px;width:132px;height:45px;background:var(--blue)}
.links{left:650px;top:3471px;font-family:'Montserrat',sans-serif;font-size:14.5px;line-height:30px;color:#fff}
.links li{list-style:none;display:flex;align-items:center;gap:12px}
.contact{left:846px;font-family:'Montserrat',sans-serif;font-size:14.5px;line-height:24px;display:flex;gap:14px;color:#fff}
.contact svg{flex:none;margin-top:4px}
.fsoc{width:31px;height:31px;border-radius:50%}
.rule{left:112px;top:3755px;width:976px;height:1px;background:#333}
.copy{left:0;width:804px;top:3784px;text-align:center;font-family:'Montserrat',sans-serif;font-size:14.5px;color:#fff}
</style>
</head>
<body>

<!-- header -->
<div class="abs brand"><span class="brand-dot"></span><span class="brand-name">LAKELINE</span></div>
<div class="abs topbar">
  <span class="abs follow">Follow us :</span>
  <span class="abs soc" style="left:148px"><svg width="16" height="16" viewBox="0 0 24 24"><path d="M6.6 10.8c1.4 2.8 3.8 5.1 6.6 6.6l2.2-2.2c.3-.3.7-.4 1-.2 1.1.4 2.3.6 3.6.6.6 0 1 .4 1 1V20c0 .6-.4 1-1 1C10.6 21 3 13.4 3 4c0-.6.4-1 1-1h3.5c.6 0 1 .4 1 1 0 1.3.2 2.5.6 3.6.1.3 0 .7-.2 1z" fill="#fff"/></svg></span>
  <span class="abs soc" style="left:194px"></span>
  <span class="abs soc" style="left:240px"></span>
  <span class="abs soc" style="left:285px"></span>
  <div class="abs call"><span class="call-ico"><svg width="18" height="18" viewBox="0 0 24 24"><path d="M6.6 10.8c1.4 2.8 3.8 5.1 6.6 6.6l2.2-2.2c.3-.3.7-.4 1-.2 1.1.4 2.3.6 3.6.6.6 0 1 .4 1 1V20c0 .6-.4 1-1 1C10.6 21 3 13.4 3 4c0-.6.4-1 1-1h3.5c.6 0 1 .4 1 1 0 1.3.2 2.5.6 3.6.1.3 0 .7-.2 1z" fill="#0677BA"/></svg></span>Call us today : +1 603 555 0142</div>
</div>
<nav class="abs nav"><span class="active">HOME</span><span>WHAT WE DO</span><span>CALENDAR BOOKING</span><span>MISSION</span><span>BLOG</span><span>CONTACT US</span></nav>

<!-- hero -->
<section class="abs hero">
  <div class="hero-photo" role="img" aria-label="Cabin cruiser on stands in a boatyard under a blue sky"></div>
  <h1>LAKELINE MARINE</h1>
  <span class="btn">GET STARTED</span>
  <span class="arrow abs" style="left:33px;top:306px"><svg width="12" height="12" viewBox="0 0 12 12"><path d="M8 1 3 6l5 5" fill="none" stroke="#333" stroke-width="1.5"/></svg></span>
  <span class="arrow abs" style="left:1121px;top:306px"><svg width="12" height="12" viewBox="0 0 12 12"><path d="M4 1l5 5-5 5" fill="none" stroke="#333" stroke-width="1.5"/></svg></span>
  <div class="dots"><i></i><i class="on"></i><i></i></div>
  <svg class="abs" style="left:0;top:0" width="1200" height="678" viewBox="0 0 1200 678">
    <path d="M0,560 C150,520 300,560 460,620 C600,660 760,686 880,678 C700,690 520,660 380,632 C220,604 100,640 0,690 Z" fill="#0677BA"/>
    <path d="M0,690 C100,642 220,612 380,638 C560,668 720,690 880,678 L1200,600 L1200,678 L0,678 Z" fill="#fff"/>
    <path d="M330,484 C450,530 600,596 834,596 C980,592 1100,540 1200,500 L1200,560 C1100,610 980,650 834,646 C640,640 480,570 330,484 Z" fill="#EE7325"/>
  </svg>
</section>

<!-- what we do -->
<h2 class="abs section-title wwd-title">WHAT WE DO</h2>
<p class="abs wwd-text">We aim to run a company focused on providing customers in the lakes region of the central New Hampshire with a broad range of boats and cars services, including but not limited to shrink wrap for boats, mobile detailing for boats and cars, mobile winterization for boats and much more. We already own a company operating a floating bar and restaurant on Lake Winnipesaukee with a strong social media following and want to leverage on our existing audience to obtain hundreds of thousands of views and interactions every day to nurture positive word of mouth and organic advertising. The New Hampshire lakes region is extremely busy and with not so many competitors and no more dock spaces or valets available in the region we believe our venture will be a great success, especially considering the steep growth in boat sales recently observed.</p>
<span class="abs btn wwd-btn">LEARN MORE</span>

<!-- booking -->
<div class="abs booking-bg"></div>
<svg class="abs" style="left:0;top:1250px" width="1200" height="170" viewBox="0 0 1200 170">
  <path d="M0,100 C120,50 220,26 330,28 C520,30 700,110 880,150 C1000,170 1120,110 1200,80 L1200,0 L0,0 Z" fill="#fff"/>
  <path d="M170,50 C230,32 280,27 330,28 C520,30 700,110 880,150 C1000,170 1120,110 1200,80 L1200,92 C1120,126 1010,170 880,156 C700,120 520,36 330,30 C280,29 230,36 170,50 Z" fill="#0677BA"/>
</svg>
<h2 class="abs section-title booking-title">CALENDAR BOOKING</h2>

<article class="abs event" style="top:1471px">
  <div class="pic" role="img" aria-label="Crew securing a cargo ship at the quay" style="background:linear-gradient(160deg,#7fb3d9,#8b5a4a 60%,#5f8ea8)"></div>
  <h3>Lorem ipsum dolor sit am consectetur adipiscing</h3>
  <span class="date"><svg width="12" height="12" viewBox="0 0 12 12"><rect x="1" y="2" width="10" height="9" fill="none" stroke="#0677BA"/><path d="M1 5h10M4 1v2M8 1v2" stroke="#0677BA"/></svg>15, Sep 2021</span>
  <p>Lorem ipsum dolor sit amet, consec tetur adipiscing elit, sed do eiusmod tempor incididunt ut labore</p>
</article>
<article class="abs event" style="top:1669px">
  <div class="pic" role="img" aria-label="White bow rider on a trailer" style="background:linear-gradient(160deg,#dfe5ea,#f5f5f5 50%,#8a9aa8)"></div>
  <h3>Lorem ipsum dolor sit am consectetur adipiscing</h3>
  <span class="date"><svg width="12" height="12" viewBox="0 0 12 12"><rect x="1" y="2" width="10" height="9" fill="none" stroke="#0677BA"/><path d="M1 5h10M4 1v2M8 1v2" stroke="#0677BA"/></svg>15, Sep 2021</span>
  <p>Lorem ipsum dolor sit amet, consec tetur adipiscing elit, sed do eiusmod tempor incididunt ut labore</p>
</article>

<div class="abs cal">
  <div class="cal-head"><span>SEPTEMBER 2021</span><svg width="20" height="12" viewBox="0 0 20 12"><path d="M8 1 2 6l6 5zM12 1l6 5-6 5z" fill="#fff"/></svg></div>
  <div class="cal-grid">
    <div class="dn">Monday</div><div class="dn">Tuesday</div><div class="dn">Wednesday</div><div class="dn">Thursday</div><div class="dn">Friday</div><div class="dn">Saturday</div><div class="dn sun">Sunday</div>
    <div class="d"></div><div class="d"></div><div class="d">1</div><div class="d">2</div><div class="d">3</div><div class="d">4</div><div class="d sun">5</div>
    <div class="d">6</div><div class="d">7</div><div class="d">8</div><div class="d">9</div><div class="d">10</div><div class="d">11</div><div class="d sun">12</div>
    <div class="d">13</div><div class="d">14</div><div class="d sel">15</div><div class="d">16</div><div class="d">17</div><div class="d book">18</div><div class="d sun">19</div>
    <div class="d">20</div><div class="d">21</div><div class="d">22</div><div class="d">23</div><div class="d">24</div><div class="d">25</div><div class="d sun">26</div>
    <div class="d">27</div><div class="d">28</div><div class="d">29</div><div class="d">30</div><div class="d"></div><div class="d"></div><div class="d sun"></div>
  </div>
</div>

<!-- mission -->
<section class="abs mission" role="img" aria-label="Workers in safety gear on a lift beside a ship hull, tinted orange">
  <div class="kicker">OUR MISSION</div>
  <h2>WE AIM TO RUN A COMPANY FOCUSED ON PROVIDING CUSTOMERS IN THE LAKES REGION OF THE CENTRAL NEW HAMPSHIRE WITH A BROAD RANGE OF PREMIUM BOATS AND CARS SERVICES.</h2>
  <p>We are on a mission to support boat and car owners to keep their vessels and cars clean, well maintained, protected and safe wherever they are at convenient prices.</p>
  <svg class="abs" style="left:0;top:0" width="1200" height="620" viewBox="0 0 1200 620">
    <path d="M0,550 C250,440 480,600 780,590 C980,584 1100,540 1200,520 L1200,620 L0,620 Z" fill="#fff"/>
  </svg>
</section>

<!-- blog -->
<h2 class="abs section-title blog-title">OUR LATEST BLOG</h2>
<span class="arrow abs" style="left:33px;top:2918px;background:#eee"><svg width="12" height="12" viewBox="0 0 12 12"><path d="M8 1 3 6l5 5" fill="none" stroke="#333" stroke-width="1.5"/></svg></span>
<span class="arrow abs" style="left:1121px;top:2918px;background:#eee"><svg width="12" height="12" viewBox="0 0 12 12"><path d="M4 1l5 5-5 5" fill="none" stroke="#333" stroke-width="1.5"/></svg></span>

<article class="abs post" style="left:112px">
  <div class="pic" role="img" aria-label="Technician with tablet at an engine room control panel" style="background:linear-gradient(135deg,#5d6f5c,#a7a489 50%,#33423e)"></div>
  <h3>Lorem ipsum dolor sit amet, consectetur</h3>
  <p>Lorem ipsum dolor sit amet, consectetur adipiscing elit, sed do eiusmod tempor incididunt ut labore et dolo</p>
  <a>Learn more <svg width="12" height="12" viewBox="0 0 12 12"><circle cx="6" cy="6" r="6" fill="#0054AA"/><path d="M5 3l3 3-3 3" fill="none" stroke="#fff" stroke-width="1.5"/></svg></a>
</article>
<article class="abs post" style="left:444px">
  <div class="pic" role="img" aria-label="Two workers on a lift painting a hull" style="background:linear-gradient(135deg,#8b3a3e,#b9a7a5 50%,#4e6f86)"></div>
  <h3>Lorem ipsum dolor sit amet, consectetur</h3>
  <p>Lorem ipsum dolor sit amet, consectetur adipiscing elit, sed do eiusmod tempor incididunt ut labore et dolo</p>
  <a>Learn more <svg width="12" height="12" viewBox="0 0 12 12"><circle cx="6" cy="6" r="6" fill="#0054AA"/><path d="M5 3l3 3-3 3" fill="none" stroke="#fff" stroke-width="1.5"/></svg></a>
</article>
<article class="abs post" style="left:776px">
  <div class="pic" role="img" aria-label="Ship on calm water at sunset" style="background:linear-gradient(180deg,#e8a85a,#f4c97a 45%,#6b4a3a 75%,#2e2a2a)"></div>
  <h3>Lorem ipsum dolor sit amet, consectetur</h3>
  <p>Lorem ipsum dolor sit amet, consectetur adipiscing elit, sed do eiusmod tempor incididunt ut labore et dolo</p>
  <a>Learn more <svg width="12" height="12" viewBox="0 0 12 12"><circle cx="6" cy="6" r="6" fill="#0054AA"/><path d="M5 3l3 3-3 3" fill="none" stroke="#fff" stroke-width="1.5"/></svg></a>
</article>

<!-- footer -->
<footer class="abs footer"></footer>
<svg class="abs" style="left:0;top:3190px" width="1200" height="210" viewBox="0 0 1200 210">
  <path d="M0,70 C300,40 600,60 900,92 C1050,104 1150,72 1200,42 L1200,210 L0,210 Z" fill="#000"/>
  <path d="M330,45 C600,60 850,112 1000,112 C1100,112 1160,82 1200,62 L1200,10 C1120,42 1050,62 950,57 C750,47 500,30 330,45 Z" fill="#0677BA"/>
  <path d="M0,130 C200,100 400,140 600,170 C720,185 820,185 880,182 C700,200 500,192 300,172 C180,160 80,172 0,192 Z" fill="#EE7325"/>
</svg>

<h4 class="abs f-h" style="left:112px;top:3434px">GET IN TOUCH</h4>
<div class="abs field" style="left:112px;top:3482px;width:234px;height:38px">First Name</div>
<div class="abs field" style="left:353px;top:3482px;width:236px;height:38px">Last Name</div>
<div class="abs field" style="left:112px;top:3531px;width:234px;height:38px">Email</div>
<div class="abs field" style="left:353px;top:3531px;width:236px;height:38px">phone number</div>
<div class="abs field" style="left:112px;top:3580px;width:477px;height:73px">Message</div>
<span class="abs btn submit">SUBMIT</span>

<h4 class="abs f-h" style="left:650px;top:3434px">QUICK LINKS</h4>
<ul class="abs links">
  <li><span>»</span>Home</li><li><span>»</span>About Us</li><li><span>»</span>Services</li><li><span>»</span>Contact Us</li><li><span>»</span>Privacy policy</li>
</ul>

<h4 class="abs f-h" style="left:846px;top:3434px">CONTACT US</h4>
<div class="abs contact" style="top:3479px"><svg width="12" height="14" viewBox="0 0 12 14"><path d="M6 0a5 5 0 0 1 5 5c0 4-5 9-5 9S1 9 1 5a5 5 0 0 1 5-5z" fill="#fff"/><circle cx="6" cy="5" r="2" fill="#000"/></svg><span style="width:230px;padding-left:8px">270 Lorem ipsum dolor amet, consectetur elit,</span></div>
<div class="abs contact" style="top:3537px"><svg width="10" height="14" viewBox="0 0 10 14"><rect x="1" y="0" width="8" height="14" rx="1" fill="#fff"/><rect x="2.5" y="2" width="5" height="8" fill="#000"/></svg><span style="padding-left:4px">(603) 555 0187</span></div>
<div class="abs contact" style="top:3571px"><svg width="14" height="14" viewBox="0 0 14 14"><rect x="0" y="4" width="14" height="10" fill="#fff"/><rect x="3" y="0" width="8" height="5" fill="#fff"/><rect x="3" y="7" width="8" height="2" fill="#000"/></svg><span>(603) 555 0190</span></div>
<div class="abs contact" style="top:3604px"><svg width="14" height="12" viewBox="0 0 14 12"><rect x=".7" y=".7" width="12.6" height="10.6" fill="none" stroke="#fff" stroke-width="1.4"/><path d="M1 1l6 5 6-5" fill="none" stroke="#fff" stroke-width="1.4"/></svg><span>hello@lakelinemarine.com</span></div>

<h4 class="abs f-h" style="left:650px;top:3660px">STAY CONNECTED :</h4>
<span class="abs fsoc" style="left:850px;top:3656px;background:#3b5bb0"></span>
<span class="abs fsoc" style="left:889px;top:3656px;background:#c1359a"></span>

<div class="abs rule"></div>
<div class="abs copy">© 2021 Lakeline Marine &nbsp;| All Rights Reserved | Terms and Conditions</div>

</body>
</html>
```